Business cards, stationery and report cover
For market research and marketing company in New Zealand
Simple
Rosalind Thorpe
Level 1
57 Pemberly Road
Milford
Auckland
PO Box 46-582
Auckland 0963
rosalind@lumenvex.co.nz
www.lumenvex.co.nz
From this process we are looking for business cards, letterhead, comp slip, as well as a generic cover page and inside page for our reports (e.g heading styles, footers etc). Both report pages need to be easily replicated or applied to Microsoft Word reports. We are PC users if this makes a difference.
The information for the business cards can be on the front or the back - depending on your design and what looks best. Most people would contact us by phone/cell/email.
We would like to be viewed as professional, competent, modern and well established. We don't want to look like we are an advertising agency, or quirky or too different from our competitors. However, we'd like to be eye catching and interesting! Our typical clients are intelligent managers who are over 35 years and a mixture of male and female.
Please let us know if you have any questions or would like clarification on anything.
As noted in 'Additional Comments' you can choose what details would look best on the front of the business card, and which you would recommend going on the back of the card.
This is our new logo.

```html
<!DOCTYPE html>
<html lang="en">
<head>
<meta charset="utf-8">
<title>Lumenvex stationery set</title>
<link href="https://fonts.googleapis.com/css2?family=Open+Sans:wght@300;400;600&display=swap" rel="stylesheet">
<style>
  :root {
    --stage: #e9e5df;
    --paper: #ffffff;
    --brand-blue: #2f7fc8;
    --brand-blue-deep: #236aae;
    --ink: #5a5f66;
    --ink-soft: #9aa0a6;
    --flap-grey: #7d8288;
    --shadow: rgba(0,0,0,.18);
  }
  * { box-sizing: border-box; margin: 0; padding: 0; }
  html, body { width: 1200px; height: 281px; overflow: hidden; }
  body {
    background: var(--stage);
    font-family: "Open Sans", Arial, sans-serif;
    color: var(--ink);
    position: relative;
  }
  .sheet {
    position: absolute;
    background: var(--paper);
    box-shadow: 0 1px 4px var(--shadow);
    overflow: hidden;
  }
  .wordmark {
    font-weight: 300;
    color: var(--brand-blue);
    letter-spacing: .01em;
    line-height: 1;
    white-space: nowrap;
  }
  .tagline { font-size: 3px; color: var(--ink-soft); letter-spacing: .1em; }
  .fine { font-size: 3.2px; line-height: 1.45; color: var(--ink); }

  /* business cards */
  .card { left: 12px; width: 108px; height: 62px; }
  .card--details { top: 50px; padding: 6px 7px; }
  .card--details .wordmark { font-size: 9px; position: absolute; right: 7px; top: 6px; }
  .card--details .name { font-size: 4.5px; font-weight: 600; color: var(--brand-blue); margin-top: 18px; }
  .card--logo { top: 124px; display: flex; align-items: center; justify-content: center; }
  .card--logo .wordmark { font-size: 15px; }
  .card--blue { top: 196px; background: var(--brand-blue); display: flex; align-items: center; justify-content: center; }
  .card--blue .wordmark { color: #fff; font-size: 15px; }

  /* letterhead */
  .letterhead { top: 22px; width: 158px; height: 224px; }
  .letterhead--one { left: 142px; }
  .letterhead--two { left: 314px; }
  .letterhead .wordmark { position: absolute; right: 12px; top: 12px; font-size: 11px; }
  .letterhead .address { position: absolute; right: 12px; top: 28px; text-align: right; font-size: 2.6px; color: var(--ink-soft); line-height: 1.4; }
  .letterhead .footer { position: absolute; left: 0; right: 0; bottom: 8px; text-align: center; font-size: 2.6px; color: var(--ink-soft); }
  .letterhead .edge { position: absolute; right: 0; top: 0; width: 3px; height: 40px; background: var(--brand-blue); }

  /* report covers */
  .cover { top: 18px; width: 162px; height: 232px; }
  .cover--white { left: 506px; }
  .cover--white .wordmark { position: absolute; left: 0; right: 0; text-align: center; top: 88px; font-size: 24px; }
  .cover--white .tagline { position: absolute; left: 0; right: 0; text-align: center; top: 116px; }
  .cover--white .title { position: absolute; left: 0; right: 0; text-align: center; bottom: 32px; font-size: 12px; color: var(--brand-blue); }
  .cover--blue { left: 690px; }
  .cover--blue .head { height: 78px; display: flex; align-items: center; justify-content: center; }
  .cover--blue .head .wordmark { font-size: 20px; }
  .cover--blue .body { position: absolute; top: 78px; left: 0; right: 0; bottom: 0; background: var(--brand-blue); }
  .cover--blue .title { position: absolute; left: 0; right: 0; text-align: center; bottom: 56px; font-size: 12px; color: #fff; }

  /* envelopes */
  .envelope { left: 880px; width: 230px; height: 96px; }
  .envelope--back { top: 20px; }
  .envelope--front { top: 130px; }
  .envelope--small { top: 180px; left: 900px; width: 210px; height: 80px; }
  .envelope svg { position: absolute; inset: 0; }
  .envelope .wordmark { position: absolute; left: 10px; top: 10px; font-size: 9px; }
  .envelope .band { position: absolute; left: 0; right: 0; bottom: 0; height: 10px; background: var(--brand-blue); }
</style>
</head>
<body>

  <!-- business cards -->
  <section class="sheet card card--details">
    <div class="wordmark">lumenvex</div>
    <p class="name">Rosalind Thorpe</p>
    <p class="fine">57 Pemberly Road<br>PO Box 46-582, Auckland 0963<br>rosalind@lumenvex.co.nz<br>www.lumenvex.co.nz</p>
  </section>
  <section class="sheet card card--logo"><div class="wordmark">lumenvex</div></section>
  <section class="sheet card card--blue"><div class="wordmark">lumenvex</div></section>

  <!-- letterheads -->
  <section class="sheet letterhead letterhead--one">
    <div class="wordmark">lumenvex</div>
    <p class="address">57 Pemberly Road<br>PO Box 46-582<br>Auckland 0963</p>
    <p class="footer">www.lumenvex.co.nz · rosalind@lumenvex.co.nz</p>
  </section>
  <section class="sheet letterhead letterhead--two">
    <span class="edge"></span>
    <p class="footer">57 Pemberly Road · Milford · Auckland 0963 · www.lumenvex.co.nz</p>
  </section>

  <!-- report covers -->
  <section class="sheet cover cover--white">
    <div class="wordmark">lumenvex</div>
    <p class="tagline">MARKET RESEARCH &amp; MARKETING</p>
    <h2 class="title">Project Title</h2>
  </section>
  <section class="sheet cover cover--blue">
    <div class="head"><div class="wordmark">lumenvex</div></div>
    <div class="body"><h2 class="title">Project Title</h2></div>
  </section>

  <!-- envelopes -->
  <section class="sheet envelope envelope--back">
    <svg viewBox="0 0 230 96" width="230" height="96" aria-hidden="true">
      <polygon points="0,0 230,0 115,44" fill="var(--flap-grey)"/>
    </svg>
  </section>
  <section class="sheet envelope envelope--front">
    <div class="wordmark">lumenvex</div>
    <span class="band"></span>
  </section>
  <section class="sheet envelope envelope--small">
    <div class="wordmark">lumenvex</div>
    <span class="band"></span>
  </section>

</body>
</html>
```